Comp & Pen Prep Tip Sheet for Veterans

I need a flyer/brochure/card with tips to help prepare veterans for their upcoming Comp & Pen Exams. Needs to be colorful and have vectors/images that correspond with teach tip. I have attached a word document with the language to include. This will go out with our welcome kit for veterans to reference before their exam.

Target Market(s)

Veterans

Industry/Entity Type

Legal/Non-Profit Organization/Medical

Colors
0054AA
0677BA
7BADD7
CADEEF
E8F1F8

Requirements
Must have
• Vectors/easy to follow

```html
<!DOCTYPE html>
<html lang="en">
<head>
<meta charset="utf-8">
<title>Things to Remember For Your Exam</title>
<link href="https://fonts.googleapis.com/css2?family=Oswald:wght@700&family=Fira+Sans:wght@400;600;700&display=swap" rel="stylesheet">
<style>
  :root {
    --blue-top: #0a5ec6;
    --blue-bottom: #0b3a7e;
    --title-blue: #0a4e9e;
    --accent-red: #b3202b;
    --ink: #1f2a36;
    --sheet: #f2f3f5;
    --white: #ffffff;
    --icon-blue: #1d4f9c;
  }
  * { margin: 0; padding: 0; box-sizing: border-box; }
  html, body { width: 1200px; height: 849px; overflow: hidden; }
  body { font-family: "Fira Sans", sans-serif; background: var(--sheet); }
  .flyer { position: relative; width: 1200px; height: 849px; background: var(--sheet); }

  .sidebar {
    position: absolute; left: 0; top: 0; width: 396px; height: 849px;
    background: linear-gradient(180deg, var(--blue-top) 0%, #0a4ea8 45%, var(--blue-bottom) 100%);
    color: var(--white);
  }
  .brand {
    position: absolute; left: 37px; top: 120px; width: 220px;
    display: flex; align-items: center; justify-content: center; gap: 10px;
  }
  .brand-dot { width: 22px; height: 22px; border-radius: 50%; background: var(--white); flex: none; }
  .brand-name { font-weight: 700; font-size: 22px; line-height: 26px; color: var(--white); }
  .brand-since {
    position: absolute; left: 37px; top: 246px; width: 220px; text-align: center;
    font-weight: 600; font-size: 12px; color: var(--white);
  }
  .intro { position: absolute; left: 37px; top: 300px; width: 318px; }
  .intro p { font-size: 14.6px; line-height: 18.1px; margin-bottom: 18.1px; }
  .reminder-bar { position: absolute; left: 37px; width: 325px; height: 5px; background: var(--accent-red); }
  .reminder-bar.top { top: 649px; }
  .reminder-bar.bottom { top: 778px; }
  .reminder {
    position: absolute; left: 37px; top: 666px; width: 325px;
    font-weight: 700; font-size: 19px; line-height: 24px; text-transform: uppercase;
  }

  .title {
    position: absolute; left: 432px; top: 62px;
    font-family: "Oswald", sans-serif; font-weight: 700; font-size: 48px; line-height: 64px;
    color: var(--accent-red); letter-spacing: -0.5px; white-space: nowrap;
  }
  .title .accent { color: var(--title-blue); }

  .tip { position: absolute; width: 232px; }
  .tip svg { display: block; height: 68px; width: 68px; }
  .tip h2 { font-size: 17px; font-weight: 700; color: var(--accent-red); margin-top: 8px; line-height: 20px; }
  .tip p { font-size: 13px; line-height: 17px; color: var(--ink); margin-top: 8px; }
  .tip p + p { margin-top: 17px; }
  .col1 { left: 434px; } .col2 { left: 686px; } .col3 { left: 934px; }
  .row1 { top: 166px; } .row2 { top: 500px; }
</style>
</head>
<body>
<main class="flyer">
  <aside class="sidebar">
    <div class="brand"><span class="brand-dot"></span><span class="brand-name">Harbor Veterans Outreach</span></div>
    <div class="brand-since">Serving Veterans With Pride</div>
    <div class="intro">
      <p>The Comp &amp; Pen Exam is your opportunity to present all the reasons you believe your condition is related to service to the physician.</p>
      <p>If your condition is not already service-connected, be sure to talk to the examiner about what happened in service that could have led to your current condition. The examiner will review your file, including your statements, service records, and treatment records, and provide a medical opinion as to whether your condition was caused or aggravated by your military service.</p>
      <p>The examiner will be observing your movements and behavior and may perform a limited physical exam to evaluate your condition.</p>
    </div>
    <div class="reminder-bar top"></div>
    <p class="reminder">After your Comp &amp; Pen exam, make sure you complete the Comp &amp; Pen exit survey based on your experience</p>
    <div class="reminder-bar bottom"></div>
  </aside>

  <h1 class="title">Things to Remember <span class="accent">For Your Exam</span></h1>

  <section class="tip col1 row1">
    <svg viewBox="0 0 68 68" aria-hidden="true" fill="none" stroke-width="2.2">
      <path d="M20 4a16 14 0 1 1-8 26l-8 4 4-8A16 14 0 0 1 20 4z" stroke="var(--accent-red)"/>
      <g fill="var(--ink)"><circle cx="14" cy="18" r="1.6"/><circle cx="20" cy="18" r="1.6"/><circle cx="26" cy="18" r="1.6"/></g>
      <path d="M44 30a15 13 0 1 0 8 24l8 4-3-8A15 13 0 0 0 44 30z" stroke="var(--icon-blue)"/>
      <g fill="var(--ink)"><circle cx="38" cy="43" r="1.6"/><circle cx="44" cy="43" r="1.6"/><circle cx="50" cy="43" r="1.6"/></g>
    </svg>
    <h2>Talk About Your Service</h2>
    <p>Talk about what happened in service that you believe caused or aggravated your condition. Try to be as specific as possible. If you are not comfortable discussing the details of an in-service event, you may point to statements you submitted to the benefits office previously for the examiner to reference. If you can, provide the examiner with a copy of these statements on the day of the exam.</p>
  </section>

  <section class="tip col2 row1">
    <svg viewBox="0 0 68 68" aria-hidden="true" fill="none" stroke-width="2.2">
      <circle cx="30" cy="30" r="24" stroke="var(--icon-blue)"/>
      <circle cx="30" cy="30" r="12" stroke="var(--icon-blue)"/>
      <path d="M26 27a4 4 0 1 1 5 4v3" stroke="var(--accent-red)"/>
      <circle cx="31" cy="38" r="1.2" fill="var(--accent-red)" stroke="none"/>
    </svg>
    <h2>Ask for Clarification</h2>
    <p>Do not answer a question you do not understand. Ask for clarification if necessary. Do not talk to fill the space or time. Keep your conversation with the examiner limited to what happened in service, the frequency and severity of symptoms related to your condition, and how they impact your day-to-day life.</p>
  </section>

  <section class="tip col3 row1">
    <svg viewBox="0 0 68 68" aria-hidden="true" fill="none" stroke-width="2.2">
      <path d="M26 46C10 34 2 26 2 16 2 8 8 3 14 3c5 0 9 3 12 7 3-4 7-7 12-7 6 0 12 5 12 13 0 10-8 18-24 30z" stroke="var(--accent-red)"/>
      <circle cx="26" cy="24" r="8" stroke="var(--icon-blue)"/>
      <path d="M22 24l3 3 5-6" stroke="var(--icon-blue)"/>
      <path d="M2 58h12c6 0 10-4 16-4h10c2 0 2 3 0 3H28M2 64h20c8 0 18-8 24-12" stroke="var(--icon-blue)"/>
    </svg>
    <h2>Be Honest</h2>
    <p>Be honest when describing the frequency and severity of your symptoms and how they impact your day-to-day life to the examiner; do not downplay the severity of your symptoms.</p>
    <p>Keep in mind that the examiner will be closely monitoring your movements and behavior, including your body language and the tone of your voice.</p>
  </section>

  <section class="tip col1 row2">
    <svg viewBox="0 0 68 68" aria-hidden="true" fill="none" stroke-width="2.2">
      <circle cx="30" cy="30" r="24" stroke="var(--icon-blue)"/>
      <path d="M32 10l-8 16h10l-8 18" stroke="var(--accent-red)"/>
      <path d="M14 20l6 4M46 20l-6 4M12 36l7-2M48 36l-7-2" stroke="var(--accent-red)"/>
    </svg>
    <h2>Pain</h2>
    <p>While the exam is not meant to be painful, you may experience slight discomfort depending on the required testing.</p>
    <p>When testing your range of motion, be sure to tell the examiner AS SOON AS you begin to experience pain, as this contributes to your overall functional loss and should be considered in your rating.</p>
  </section>

  <section class="tip col2 row2">
    <svg viewBox="0 0 68 68" aria-hidden="true" fill="none" stroke-width="2.2">
      <rect x="2" y="2" width="52" height="62" rx="2" stroke="var(--icon-blue)"/>
      <path d="M36 26c-8-5-12-9-12-13 0-3 2-5 5-5 3 0 5 2 7 4 2-2 4-4 7-4 3 0 5 2 5 5 0 4-4 8-12 13z" stroke="var(--accent-red)"/>
      <path d="M9 34l3 3 5-5M9 44l3 3 5-5M9 54l3 3 5-5M22 36h24M22 46h24M22 56h24" stroke="var(--icon-blue)"/>
    </svg>
    <h2>Trace Your Symptoms</h2>
    <p>Discuss what symptoms you experienced immediately following your injury in service and how these symptoms have worsened over time.</p>
    <p>Your statement will help trace the start of your symptoms back to what happened during service.</p>
  </section>

  <section class="tip col3 row2">
    <svg viewBox="0 0 68 68" aria-hidden="true" fill="none" stroke-width="2.2">
      <rect x="2" y="2" width="36" height="62" rx="3" stroke="var(--icon-blue)"/>
      <g stroke="var(--accent-red)">
        <circle cx="11" cy="13" r="3.5"/><circle cx="25" cy="13" r="3.5"/>
        <circle cx="11" cy="27" r="3.5"/><circle cx="25" cy="27" r="3.5"/>
        <circle cx="11" cy="41" r="3.5"/><circle cx="25" cy="41" r="3.5"/>
        <circle cx="11" cy="55" r="3.5"/><circle cx="25" cy="55" r="3.5"/>
      </g>
      <rect x="32" y="18" width="30" height="6" rx="1" stroke="var(--icon-blue)" fill="var(--sheet)"/>
      <rect x="34" y="24" width="26" height="40" rx="2" stroke="var(--icon-blue)" fill="var(--sheet)"/>
      <path d="M34 34h26M34 54h26" stroke="var(--icon-blue)"/>
      <path d="M47 39v10M42 44h10" stroke="var(--accent-red)"/>
    </svg>
    <h2>Medications</h2>
    <p>If you are prescribed any medication(s) for your condition, be sure to tell the examiner the name and dosage of each medication and how often you take each. This is extremely important, because medication may mask some of your symptoms, or the use of medication(s) may be used to evaluate the severity of your condition and how much it impacts your ability to work.</p>
  </section>
</main>
</body>
</html>
```